Church Christmas Flyer

The flyer is to advertise our Christmas Eve services. The flyer is for a Christian church service to celebrate the birth of Jesus. We would like to see designs that use blue, silver and gold for colors but feel free to be creative. We are interested in a flyer that is has texture, depth and is more abstract than literal. Don't be afraid to layer. Please make the flyer double sided

* I uploaded our Christmas flyer from last year.

Target Market(s)

30-55 year old, male and female

Industry/Entity Type

Church

Requirements
Must have
• Map to the church
Church phone number 555-317-4096
Service times 3:00pm and 5:00pm
church address 28315 Marigold Ave, Larkmont, Ca. 93781
church website www.brookfieldfellowshipnt.com
Scripture verse

Text must stand out and be easy to read
Nice to have
• Use of the star in the sky that guided the wise men to Jesus.
Should not have
• Santa Clause, Snowmen, Reindeer

```html
<!DOCTYPE html>
<html lang="en">
<head>
<meta charset="utf-8">
<title>Christmas Eve Celebration Service</title>
<link rel="stylesheet" href="https://fonts.googleapis.com/css2?family=Cormorant+Garamond:ital,wght@0,600;1,700&family=Comfortaa:wght@400;700&family=Lato:wght@700&display=swap">
<style>
  :root {
    --violet-deep: #6f6a92;
    --violet-mid: #9c97b8;
    --violet-light: #c9c5dc;
    --lavender-pale: #dcd9e8;
    --star-white: #ffffff;
    --gold: #d9b45a;
    --gold-light: #f2d98a;
    --text-white: #f7f5fb;
    --ink-navy: #1d2350;
    --map-cream: #ece6d6;
    --logo-ink: #3c3a4a;
  }
  html, body {
    margin: 0;
    padding: 0;
    width: 900px;
    height: 1200px;
    overflow: hidden;
    background: var(--violet-light);
  }
  .flyer {
    position: relative;
    width: 900px;
    height: 1200px;
    overflow: hidden;
    background:
      linear-gradient(180deg, rgba(255,255,255,0) 62%, var(--lavender-pale) 100%),
      linear-gradient(120deg, var(--violet-mid) 0%, var(--violet-deep) 35%, var(--violet-mid) 65%, var(--violet-light) 100%);
    font-family: "Lato", sans-serif;
  }
  .star-glow {
    position: absolute;
    left: 0;
    top: 0;
    width: 420px;
    height: 560px;
  }
  .scripture {
    position: absolute;
    left: 372px;
    top: 30px;
    width: 500px;
    margin: 0;
    font-family: "Comfortaa", sans-serif;
    font-size: 22px;
    line-height: 1.3;
    color: var(--text-white);
  }
  .scripture .line { display: block; white-space: nowrap; }
  .scripture .last { display: flex; justify-content: space-between; padding-right: 30px; }
  .scripture cite { font-style: italic; }
  .invitation {
    position: absolute;
    left: 330px;
    top: 205px;
    width: 510px;
    text-align: center;
    font-family: "Cormorant Garamond", serif;
    color: var(--gold);
    text-shadow: 0 0 8px rgba(255, 230, 160, 0.55), 1px 1px 1px rgba(60, 50, 20, 0.5);
  }
  .invitation .join {
    margin: 0 0 10px;
    font-style: italic;
    font-weight: 700;
    font-size: 48px;
    line-height: 1.05;
  }
  .invitation .event {
    margin: 0;
    font-weight: 600;
    font-size: 48px;
    line-height: 1.2;
    letter-spacing: 1px;
    color: var(--gold-light);
  }
  .service-times {
    position: absolute;
    left: 330px;
    top: 440px;
    width: 510px;
    margin: 0;
    text-align: center;
    font-family: "Comfortaa", sans-serif;
    font-weight: 700;
    font-size: 24px;
    letter-spacing: 1px;
    color: var(--gold-light);
  }
  .contact {
    position: absolute;
    left: 30px;
    top: 592px;
    width: 265px;
    margin: 0;
    text-align: center;
    font-style: normal;
    font-weight: 700;
    font-size: 16px;
    line-height: 1.3;
    color: var(--ink-navy);
  }
  .map-area {
    position: absolute;
    left: 300px;
    top: 516px;
    width: 516px;
    height: 490px;
    background: linear-gradient(135deg, var(--map-cream) 0%, #e2dccb 50%, #efe9db 100%);
    box-shadow: 0 2px 6px rgba(40, 30, 70, 0.35);
  }
  .church-mark {
    position: absolute;
    left: 45px;
    top: 1086px;
    width: 345px;
    height: 80px;
    background: var(--star-white);
    display: flex;
    align-items: center;
    gap: 14px;
    padding-left: 18px;
    box-sizing: border-box;
  }
  .church-mark .dot {
    width: 34px;
    height: 34px;
    border-radius: 50%;
    background: var(--logo-ink);
    flex: none;
  }
  .church-mark .name {
    font-family: "Cormorant Garamond", serif;
    font-weight: 600;
    font-size: 28px;
    color: var(--logo-ink);
  }
</style>
</head>
<body>
<main class="flyer">
  <svg class="star-glow" viewBox="0 0 420 560" role="img" aria-label="Bright guiding star shining in the sky">
    <defs>
      <radialGradient id="halo" cx="195" cy="285" r="230" gradientUnits="userSpaceOnUse">
        <stop offset="0" stop-color="#ffffff" stop-opacity="1"/>
        <stop offset="0.1" stop-color="#ffffff" stop-opacity="0.85"/>
        <stop offset="0.4" stop-color="#e4e0f2" stop-opacity="0.35"/>
        <stop offset="1" stop-color="#c9c5dc" stop-opacity="0"/>
      </radialGradient>
    </defs>
    <rect width="420" height="560" fill="url(#halo)"/>
  </svg>

  <blockquote class="scripture">
    <span class="line">Do not be afraid. I bring you good news</span>
    <span class="line">of great joy that will be for all the</span>
    <span class="line last"><span>people</span><cite>Luke ~ Chapter 2</cite></span>
  </blockquote>

  <section class="invitation">
    <p class="join">Join Us!</p>
    <p class="event">For a special Christmas<br>Eve Celebration Service</p>
  </section>

  <p class="service-times">3:00pm and 5:00pm services</p>

  <address class="contact">
    28315 Marigold Ave<br>
    Larkmont, Ca. 93781<br>
    555-317-4096 - 555-317-4096<br>
    www.brookfieldfellowshipnt.com
  </address>

  <div class="map-area" role="img" aria-label="Street map showing the route to the church"></div>

  <div class="church-mark">
    <span class="dot"></span>
    <span class="name">Brookfield Fellowship</span>
  </div>
</main>
</body>
</html>
```